Business Card for Pottery and Jewellery Designer

A new business card design is needed to accompany a newly launching pottery and jewellery website. The company logo has been attached for use. The company is called Glazewick Studio. For a sense of the vibe please see the website (it is currently under construction but this way you'll get a feel for the style) www.GlazewickStudio.com

The website font is Pontano Sans for the body of the text with Overlock for headers.

The overall look should be clean and elegant. The back side can have just the logo. The front side should have a smaller logo and the following details displayed:

Glazewick Studio
Designer: Hollis Marrow
Phone: xxx.xxx.xxxx
Email: Designer@GlazewickStudio.com

The structure of displaying this is completely up to you. Different layouts and creative methods of displaying contact info are welcome as long as it stays clean/uncluttered.

No product photographs are to be included in the design as the catalogue changes quickly.

Colour preferences lean towards elegant and understated (charcoal grey, dark navy blue etc.)

Please let me know if you have any further questions or further details required.

Target Market(s)

Target market is 30+ year old women

Industry/Entity Type

Construction

Colors
ffffff
1b1b1b
474747
d9d9d9
fafafa
0355a3

Requirements
Must have
• The submissions so far have looked very typical and don't stand out right now. They're also all in navy with very little variation. I'm looking for something that stands out a it more while still being clean-looking.
Nice to have
• I've attached a few design samples and an idea for a backdrop. It would be great to see some designs in black, white, and grey with only a hint of color.
Should not have
• Product Images

```html
<!DOCTYPE html>
<html lang="en">
<head>
<meta charset="utf-8">
<title>Glazewick Studio — Business Card</title>
<link href="https://fonts.googleapis.com/css2?family=Overlock:wght@400;700&family=Pontano+Sans&display=swap" rel="stylesheet">
<style>
  :root {
    --backdrop: #e9e6e2;
    --card-dark: #1b1b1b;
    --card-light: #fafafa;
    --card-light-edge: #d9d9d9;
    --ink-light: #ffffff;
    --ink-dark: #1b1b1b;
    --ink-mid: #474747;
    --accent: #0355a3;
  }
  html, body {
    margin: 0;
    padding: 0;
    width: 1200px;
    height: 1181px;
    overflow: hidden;
    background: var(--backdrop);
  }
  .canvas {
    position: relative;
    width: 1200px;
    height: 1181px;
  }
  .card {
    position: absolute;
    left: 206px;
    width: 787px;
    height: 453px;
    box-shadow: 0 4px 10px rgba(0,0,0,0.25);
  }
  .card--back {
    top: 82px;
    background: var(--card-dark);
  }
  .card--front {
    top: 636px;
    background: radial-gradient(ellipse at 50% 48%, #ffffff 0%, var(--card-light) 45%, var(--card-light-edge) 100%);
  }
  .studio-title {
    position: absolute;
    left: 0;
    right: 0;
    top: 201px;
    margin: 0;
    text-align: center;
    font-family: "Overlock", sans-serif;
    font-weight: 400;
    font-size: 38px;
    letter-spacing: 0.5px;
    color: var(--ink-light);
    text-transform: uppercase;
  }
  .contact {
    position: absolute;
    left: 0;
    right: 0;
    top: 186px;
    text-align: center;
  }
  .contact__name {
    margin: 0;
    font-family: "Overlock", sans-serif;
    font-weight: 700;
    font-size: 38px;
    line-height: 48px;
    color: var(--ink-dark);
  }
  .contact__line {
    margin: 0;
    font-family: "Pontano Sans", sans-serif;
    font-size: 17px;
    line-height: 26px;
    color: var(--ink-dark);
  }
  .studio-mark {
    position: absolute;
    right: 30px;
    bottom: 36px;
    display: flex;
    align-items: center;
    gap: 8px;
    font-family: "Overlock", sans-serif;
    font-weight: 400;
    font-size: 18px;
  }
  .card--back .studio-mark { color: var(--ink-light); }
  .card--front .studio-mark { color: var(--ink-dark); }
  .studio-mark__dot {
    width: 12px;
    height: 12px;
    border-radius: 50%;
    background: var(--accent);
  }
</style>
</head>
<body>
<main class="canvas">
  <section class="card card--back" aria-label="Card back">
    <h1 class="studio-title">Glazewick Studio</h1>
    <div class="studio-mark"><span class="studio-mark__dot"></span>Glazewick Studio</div>
  </section>

  <section class="card card--front" aria-label="Card front">
    <div class="contact">
      <p class="contact__name">Hollis Marrow</p>
      <p class="contact__line">Designer@GlazewickStudio.com</p>
      <p class="contact__line">555-204-3187</p>
    </div>
    <div class="studio-mark"><span class="studio-mark__dot"></span>Glazewick Studio</div>
  </section>
</main>
</body>
</html>
```